Poster for Office

Looking for an edgy, beautiful poster to hang up in my office that uses the quotes located below and potentially the image attached.
Content for poster

Title: Pell's Rules

Must have the following quotes included (punctuation and capitalization are flexible, do what you think looks the best they also don't need the quotation symbols):

"Don't order fish at a steakhouse"
"Be bold. The more you tell, the more you sell"
"admit nothing, deny everything, launch counterattack."
"avoid obviousness"
"never do anything until you're ready to do it"
"look good=feel good"
"always keep the advantage"
"never complain, never explain"
"Lay low, play dumb, keep moving"

Industry/Entity Type

Quotes

Requirements
Must have
• Title: Pell's Rules

"avoid obviousness"
"look good=feel good"

```html
<!DOCTYPE html>
<html lang="en">
<head>
<meta charset="utf-8">
<title>Pell's Rules</title>
<link href="https://fonts.googleapis.com/css2?family=Cinzel:wght@600;700;900&display=swap" rel="stylesheet">
<style>
  :root {
    --backdrop-edge: #a4a6a9;
    --backdrop-centre: #eeeeef;
    --frame-line: #6d6e70;
    --crown-gold: #f8d46f;
    --slab-black: #282828;
    --title-ink: #0e0e0e;
    --rule-ink: #f4f4f4;
  }
  * { margin: 0; padding: 0; box-sizing: border-box; }
  html, body {
    width: 844px;
    height: 1200px;
    overflow: hidden;
  }
  .poster {
    position: relative;
    width: 844px;
    height: 1200px;
    background: radial-gradient(ellipse 62% 58% at 50% 50%, var(--backdrop-centre) 0%, var(--backdrop-edge) 100%);
    border: 1px solid var(--frame-line);
    font-family: "Cinzel", serif;
  }
  .tablet {
    position: absolute;
    left: 0;
    top: 0;
    width: 844px;
    height: 1200px;
  }
  .title {
    position: absolute;
    left: 0;
    width: 844px;
    top: 186px;
    padding-left: 12px;
    text-align: center;
    font-weight: 900;
    font-size: 60px;
    line-height: 1;
    color: var(--title-ink);
    letter-spacing: 0.5px;
  }
  .rules {
    position: absolute;
    left: 114px;
    width: 617px;
    top: 422px;
    list-style: none;
    text-align: center;
    color: var(--rule-ink);
    font-weight: 700;
    font-size: 21px;
    line-height: 33px;
    letter-spacing: 0.4px;
  }
  .rule { margin-bottom: 36px; }
  .rule span { display: block; }
</style>
</head>
<body>
  <main class="poster">
    <svg class="tablet" viewBox="0 0 844 1200" aria-hidden="true">
      <path class="tablet-crown" fill="var(--crown-gold)"
            d="M114,326 L114,292 A308.5,250 0 0 1 731,292 L731,326 Z"/>
      <rect class="tablet-slab" x="114" y="326" width="617" height="840" fill="var(--slab-black)"/>
    </svg>

    <h1 class="title">Pell's Rules</h1>

    <ul class="rules">
      <li class="rule"><span>Don't order fish at a steakhouse</span></li>
      <li class="rule"><span>Be bold.</span><span>The more you tell, the more you sell</span></li>
      <li class="rule"><span>Admit nothing, deny everything,</span><span>launch counterattack</span></li>
      <li class="rule"><span>Avoid obviousness</span></li>
      <li class="rule"><span>Never do anything until</span><span>you're ready to do it</span></li>
      <li class="rule"><span>Look good=feel good</span></li>
      <li class="rule"><span>Always keep the advantage</span></li>
      <li class="rule"><span>Never complain, never explain</span></li>
      <li class="rule"><span>Lay low, play dumb, keep moving</span></li>
    </ul>
  </main>
</body>
</html>
```